Business Card Design Project

We need a business card design for our company kB7 s.r.o. The company is based in Slovakia and selling massage, yoga and meditation accessories online and offline. At the place where the offices are, we have a yoga studio, massage room, show room and shop as well. We will give the business card for customers who visit our shop or show room personally and for the new suppliers of demanded products we are visiting in the future.
I would like to have:
- small logo and datas on one side
- big logo and our main e-shops on the other side:
- www.pohodlnelavice.sk
- www.relaxnipultiky.cz
Datas:
Peter Kolar, MSc. / CEO
kB7 s.r.o.
Borovicová 742/3
938 05 Dunajská Streda
Slovak republic (Slovakia)
Office tel.: +421 (0) 917 604 382
Private tel.: +421 (0) 911 758 026
E-mail: info@kb7.sk
Web: www.kb7.sk
It is up to you if you use graphics emphasizing our profile or leave it simple and modern without pics. Looking forward to receiving your designs! Thank You!

```html
<!DOCTYPE html>
<html lang="sk">
<head>
<meta charset="utf-8">
<title>kB7 s.r.o. – business card</title>
<link href="https://fonts.googleapis.com/css2?family=Montserrat:wght@400;500;700&display=swap" rel="stylesheet">
<style>
  :root {
    --backdrop: #efefef;
    --paper: #ffffff;
    --slate: #4f5b6a;
    --orange: #f47f20;
    --ink: #4a5565;
    --light: #ffffff;
  }
  * { box-sizing: border-box; margin: 0; padding: 0; }
  html, body { width: 1200px; height: 720px; overflow: hidden; }
  body {
    background: var(--backdrop);
    font-family: "Montserrat", Arial, sans-serif;
    display: flex;
    align-items: center;
    justify-content: center;
    gap: 44px;
  }
  .card {
    position: relative;
    width: 520px;
    height: 297px;
    border-radius: 2px;
    box-shadow: 0 2px 10px rgba(0,0,0,.12);
    overflow: hidden;
  }

  /* Front side */
  .card--front { background: var(--paper); }
  .brand-large {
    position: absolute;
    left: 0; right: 0; top: 78px;
    display: flex;
    align-items: center;
    justify-content: center;
    gap: 16px;
  }
  .brand-large__dot {
    width: 30px; height: 30px; border-radius: 50%;
    background: var(--orange);
  }
  .brand-large__name {
    font-size: 92px; font-weight: 700; line-height: 1;
    color: var(--ink); letter-spacing: -2px;
  }
  .eshops {
    position: absolute;
    left: 0; right: 0; top: 206px;
    text-align: center;
    font-size: 13px; font-weight: 700;
    color: var(--ink);
  }
  .eshops__sep { color: var(--orange); margin: 0 6px; }

  /* Back side */
  .card--back { background: var(--slate); color: var(--light); }
  .brand-small {
    position: absolute;
    right: 96px; top: 34px;
    display: flex; align-items: center; gap: 8px;
  }
  .brand-small__dot {
    width: 14px; height: 14px; border-radius: 50%;
    background: var(--orange);
  }
  .brand-small__name {
    font-size: 46px; font-weight: 700; line-height: 1;
    color: var(--light); letter-spacing: -1px;
  }
  .person {
    position: absolute;
    right: 30px; top: 104px;
    text-align: right;
  }
  .person__name { font-size: 14px; font-weight: 700; margin-bottom: 10px; }
  .contact {
    list-style: none;
    font-size: 11.5px; line-height: 18px; font-weight: 400;
  }
  .contact li { display: flex; align-items: center; justify-content: flex-end; gap: 7px; }
  .contact svg { width: 11px; height: 11px; fill: var(--orange); flex: none; }
  .company {
    position: absolute;
    left: 34px; top: 150px;
  }
  .company__name { font-size: 14px; font-weight: 700; margin-bottom: 22px; }
  .company__address { font-size: 12px; line-height: 17px; font-weight: 400; }
  .card__band {
    position: absolute; left: 0; right: 0; bottom: 0; height: 26px;
    display: flex;
  }
  .card__band-white { flex: 1; background: var(--paper); }
  .card__band-orange { width: 215px; background: var(--orange); border-left: 8px solid var(--slate); }
</style>
</head>
<body>

  <section class="card card--front" aria-label="Front side">
    <div class="brand-large">
      <span class="brand-large__dot"></span>
      <span class="brand-large__name">kB7</span>
    </div>
    <p class="eshops">www.pohodlnelavice.sk<span class="eshops__sep">/</span>www.relaxnipultiky.cz</p>
  </section>

  <section class="card card--back" aria-label="Back side">
    <div class="brand-small">
      <span class="brand-small__dot"></span>
      <span class="brand-small__name">kB7</span>
    </div>

    <div class="person">
      <p class="person__name">Peter Kolar, MSc. / CEO</p>
      <ul class="contact">
        <li>+421 (0) 917 604 382
          <svg viewBox="0 0 12 12" aria-hidden="true"><path d="M2 4.5C2 3 3 2 6 2s4 1 4 2.5L8.5 5 8 3.8H4L3.5 5zM3 6h6l1 4H2z"/></svg></li>
        <li>+421 (0) 911 758 026
          <svg viewBox="0 0 12 12" aria-hidden="true"><path d="M3.5 1h5v10h-5zM4.5 2v7h3V2z"/></svg></li>
        <li>info@kb7.sk
          <svg viewBox="0 0 12 12" aria-hidden="true"><path d="M1 3h10v6H1zm1 1v.3l4 2.5 4-2.5V4zm0 1.5V8h8V5.5L6 8z"/></svg></li>
        <li>www.kb7.sk
          <svg viewBox="0 0 12 12" aria-hidden="true"><path d="M6 1a5 5 0 1 0 0 10A5 5 0 0 0 6 1zm0 1.2c.7.6 1.2 1.7 1.3 3.2H4.7C4.8 3.9 5.3 2.8 6 2.2zM2.2 6.6h1.5c.1 1.2.4 2.2.9 2.9a3.8 3.8 0 0 1-2.4-2.9zm2.5 0h2.6C7.2 8 6.7 9.1 6 9.8 5.3 9.1 4.8 8 4.7 6.6z"/></svg></li>
      </ul>
    </div>

    <div class="company">
      <p class="company__name">kB7 s.r.o.</p>
      <p class="company__address">Borovicová 742/3<br>938 05 Dunajská Streda<br>Slovak republic (Slovakia)</p>
    </div>

    <div class="card__band" aria-hidden="true">
      <span class="card__band-white"></span>
      <span class="card__band-orange"></span>
    </div>
  </section>

</body>
</html>
```